Essential Oil 15ml - package of 6

Design of a box of 6 different essential oils.
+ design of the bottle stickers
My bottles are 15ml clear blue glass.

The pictures attached are my competitors...

Target Market(s)

BRAMBLEWICK USA

Font styles to use
Serif

Requirements
Must have
• Our logo + "essential oil" and type (lavender, eucalyptus etc....)
• 15ml - 0.50 fl.oz.
• special color for the oil type.

```html
<!DOCTYPE html>
<html lang="en">
<head>
<meta charset="utf-8">
<title>Sela Dune Lemon Essential Oil Label</title>
<link rel="stylesheet" href="https://fonts.googleapis.com/css2?family=EB+Garamond:wght@400;500&family=Great+Vibes&display=swap">
<style>
  :root {
    --page: #f4f4f2;
    --label-edge: #cde4b9;
    --label-centre: #e3f0d6;
    --ink: #2b2b2b;
    --gold: #c9a13a;
    --gold-light: #ecd58a;
    --panel: #ffffff;
    --leaf: #4f8a34;
    --leaf-soft: #8dbb6a;
    --lemon: #f1c53e;
  }
  * { box-sizing: border-box; margin: 0; padding: 0; }
  html, body {
    width: 964px; height: 1200px; overflow: hidden;
    background: var(--page);
  }
  .canvas {
    position: relative; width: 964px; height: 1200px;
  }
  .label {
    position: absolute; left: 42px; top: 195px;
    width: 880px; height: 810px;
    background: linear-gradient(90deg, var(--label-edge) 0%, var(--label-centre) 50%, var(--label-edge) 100%);
    overflow: hidden;
    font-family: "EB Garamond", serif;
    color: var(--ink);
  }
  .gold-rule {
    position: absolute; top: 0; bottom: 0; width: 5px;
    background: linear-gradient(180deg, var(--gold-light), var(--gold) 50%, var(--gold-light));
  }
  .gold-rule.left { left: 306px; }
  .gold-rule.right { left: 569px; }
  .botanical {
    position: absolute; top: 250px; width: 300px; height: 530px;
    border-radius: 46% 46% 40% 40%;
    background: radial-gradient(ellipse at 50% 35%, var(--leaf) 0%, var(--leaf-soft) 55%, rgba(141,187,106,0) 75%),
                radial-gradient(ellipse at 60% 88%, var(--lemon) 0%, rgba(241,197,62,0) 45%);
    opacity: 0.85;
  }
  .botanical.left { left: 0; }
  .botanical.right { right: 0; transform: scaleX(-1); }
  .brand {
    position: absolute; left: 0; right: 0; top: 105px;
    text-align: center;
  }
  .brand-dot {
    display: block; width: 52px; height: 52px; margin: 0 auto 14px;
    border-radius: 50%; background: var(--ink);
  }
  .brand-name {
    font-size: 44px; font-weight: 500; letter-spacing: 1px; line-height: 1;
  }
  .product-kind {
    margin-top: 14px;
    font-size: 38px; font-weight: 400; letter-spacing: 2px; line-height: 1;
  }
  .purity {
    position: absolute; left: 0; right: 0; top: 468px;
    text-align: center; font-size: 30px; line-height: 1;
  }
  .oil-panel {
    position: absolute; left: 158px; top: 551px;
    width: 572px; height: 138px;
    background: var(--panel);
    border: 5px solid var(--gold);
    box-shadow: inset 0 0 0 4px var(--panel), inset 0 0 0 6px var(--gold-light);
    display: flex; align-items: center; justify-content: center;
  }
  .oil-name {
    font-family: "Great Vibes", cursive;
    font-size: 104px; line-height: 1; color: var(--ink);
    padding-top: 10px;
  }
  .volume {
    position: absolute; left: 0; right: 0; top: 762px;
    text-align: center; font-size: 28px; line-height: 1;
  }
</style>
</head>
<body>
<main class="canvas">
  <section class="label">
    <div class="botanical left" role="img" aria-label="Lemon branch illustration with leaves, blossoms and lemons"></div>
    <div class="botanical right" role="img" aria-label="Lemon branch illustration with leaves, blossoms and lemons"></div>
    <div class="gold-rule left"></div>
    <div class="gold-rule right"></div>
    <header class="brand">
      <span class="brand-dot"></span>
      <p class="brand-name">Sela Dune</p>
      <p class="product-kind">essential oil</p>
    </header>
    <p class="purity">100 % pure</p>
    <div class="oil-panel"><h1 class="oil-name">Lemon</h1></div>
    <p class="volume">15ml - 0.50 fl.oz</p>
  </section>
</main>
</body>
</html>
```